CD COVER DESIGN - Coastal Nightingale

looking for an album cover --- music from the Mediterranean - 2 PHOTOS ARE INCLUDED BELOW - you are welcome to use both or just one.

Target Market(s)

WORLD MUSIC

Industry/Entity Type

Artists

Font styles to use
Decorative

Colors

Designer to choose colors to be used in the design.

Requirements
Must have
• ORHAN DEMIRCAN (artist name)
• COASTAL NIGHTINGALE (ALBUM NAME)
• ATTACHED PHOTOS (MAY USE 1 OR BOTH)
Nice to have
• IMAGERY OF THE MEDITERRANEAN

```html
<!DOCTYPE html>
<html lang="en">
<head>
<meta charset="UTF-8">
<title>Coastal Nightingale — Orhan Demircan</title>
<link rel="stylesheet" href="https://fonts.googleapis.com/css2?family=Arimo:wght@400&display=swap">
<style>
  :root {
    --sky-top: #cfe3e0;
    --sky-mid: #efe6dc;
    --horizon: #f4e2d6;
    --sea-deep: #1f6f72;
    --sea-mid: #3a9696;
    --sea-light: #7dbdb6;
    --foam: #eef2ee;
    --rock: #2a2c2e;
    --rock-dark: #151617;
    --title-ink: #1b1b1b;
    --artist-red: #e5261b;
  }
  html, body {
    margin: 0;
    padding: 0;
    width: 1200px;
    height: 1200px;
    overflow: hidden;
    background: #ffffff;
  }
  .album-cover {
    position: relative;
    width: 1200px;
    height: 1200px;
    overflow: hidden;
    font-family: "Arimo", Arial, sans-serif;
  }
  .cover-photo {
    position: absolute;
    inset: 0;
    background:
      linear-gradient(152deg, transparent 0 58%, var(--rock) 58.3%, var(--rock-dark) 100%),
      radial-gradient(ellipse 60% 30% at 30% 68%, rgba(238, 242, 238, 0.85), transparent 70%),
      radial-gradient(ellipse 80% 14% at 20% 43%, rgba(238, 242, 238, 0.45), transparent 70%),
      linear-gradient(180deg,
        var(--sky-top) 0%,
        var(--sky-mid) 16%,
        var(--horizon) 25%,
        var(--sea-deep) 25.3%,
        var(--sea-mid) 36%,
        var(--sea-light) 50%,
        var(--foam) 78%,
        var(--foam) 100%);
  }
  .cover-titles {
    position: absolute;
    left: 75px;
    top: 89px;
    margin: 0;
  }
  .album-title {
    margin: 0;
    font-size: 45px;
    line-height: 54px;
    font-weight: 400;
    letter-spacing: 0.5px;
    color: var(--title-ink);
  }
  .artist-name {
    margin: 0;
    margin-top: 45px;
    font-size: 45px;
    line-height: 54px;
    font-weight: 400;
    letter-spacing: 0.5px;
    color: var(--artist-red);
  }
</style>
</head>
<body>
  <main class="album-cover">
    <div class="cover-photo" role="img" aria-label="Photo of a musician in a patterned shirt standing on dark coastal rocks holding a kanun, looking out over a turquoise Mediterranean sea with crashing white surf under a soft pastel sky"></div>
    <header class="cover-titles">
      <h1 class="album-title">COASTAL<br>NIGHTINGALE</h1>
      <p class="artist-name">ORHAN DEMIRCAN</p>
    </header>
  </main>
</body>
</html>
```